TK Stationary Design

Logo, Business Card, Letterhead & Email Signature Design

Target Market(s)

Legal

Colors

Designer to choose colors to be used in the design.

Requirements
Must have
• Gold and Blue are the colours to use. The TK must be inside the Gold Legal Pendulum

```html
<!DOCTYPE html>
<html lang="en">
<head>
<meta charset="utf-8">
<title>TK Kgosana Incorporated – Business Card</title>
<link href="https://fonts.googleapis.com/css2?family=Cinzel:wght@500&family=Montserrat:wght@400&display=swap" rel="stylesheet">
<style>
  :root {
    --bg: #1c1e22;
    --card-black: #050506;
    --blue: #2a6b9e;
    --blue-deep: #1f5585;
    --blue-text: #2f6fa6;
    --gold: #d4a53c;
    --gold-light: #f0cd6a;
    --gold-dark: #a87a22;
  }
  * { margin: 0; padding: 0; box-sizing: border-box; }
  html, body { width: 1200px; height: 900px; overflow: hidden; }
  body { background: var(--bg); position: relative; }

  .card {
    position: absolute;
    top: 300px;
    width: 520px;
    height: 300px;
    overflow: hidden;
  }

  /* Back: contact side */
  .card-back { left: 50px; background: var(--card-black); }
  .edge-blue {
    position: absolute; left: 0; top: 0; width: 18px; height: 58%;
    background: var(--blue);
  }
  .edge-gold {
    position: absolute; left: 0; bottom: 0; width: 18px; height: 42%;
    background: linear-gradient(90deg, var(--gold-dark), var(--gold-light), var(--gold));
  }
  .brand {
    position: absolute; left: 48px; top: 38px;
    display: flex; align-items: center; gap: 10px;
  }
  .brand-dot {
    width: 14px; height: 14px; border-radius: 50%; background: var(--gold);
  }
  .brand-name {
    font-family: "Cinzel", serif; font-weight: 500; color: var(--gold);
    font-size: 19px; letter-spacing: 2px; line-height: 1.2;
  }
  .details {
    position: absolute; right: 34px; top: 40px; width: 250px;
    font-family: "Montserrat", sans-serif; color: var(--blue-text);
    text-align: right;
  }
  .person-name {
    font-family: "Cinzel", serif; font-weight: 500; color: var(--gold);
    font-size: 20px; letter-spacing: 1px;
  }
  .person-role { font-size: 13px; margin-top: 2px; }
  .rule {
    height: 1.5px; margin: 12px 0;
    background: linear-gradient(90deg, var(--gold-dark), var(--gold-light));
  }
  .address { font-size: 13px; line-height: 1.45; }
  .contact-list { list-style: none; font-size: 13px; line-height: 1.9; }
  .contact-list li { display: flex; align-items: center; justify-content: flex-end; gap: 10px; }
  .contact-list svg { width: 13px; height: 13px; fill: var(--gold); }

  /* Front: brand side */
  .card-front {
    left: 630px;
    background: linear-gradient(160deg, var(--blue-deep), var(--blue));
    display: flex; align-items: center; justify-content: center; gap: 14px;
  }
  .card-front .brand-dot { width: 18px; height: 18px; }
  .card-front .brand-name { font-size: 26px; letter-spacing: 3px; text-align: center; }
</style>
</head>
<body>

<section class="card card-back" aria-label="Business card, contact side">
  <div class="edge-blue"></div>
  <div class="edge-gold"></div>

  <div class="brand">
    <span class="brand-dot"></span>
    <span class="brand-name">TK Kgosana<br>Incorporated</span>
  </div>

  <div class="details">
    <p class="person-name">Thabo Kgosana</p>
    <p class="person-role">Director</p>
    <div class="rule"></div>
    <p class="address">Block B Oakridge Office Park<br>24 Linden road north<br>Fairview, 2190</p>
    <div class="rule"></div>
    <ul class="contact-list">
      <li>011 555 0142
        <svg viewBox="0 0 16 16" aria-hidden="true"><path d="M3 1h3l1.5 4-2 1.3a9 9 0 0 0 4.2 4.2L11 8.5l4 1.5v3a2 2 0 0 1-2 2A13 13 0 0 1 1 3a2 2 0 0 1 2-2z"/></svg>
      </li>
      <li>086 555 0198
        <svg viewBox="0 0 16 16" aria-hidden="true"><path d="M4 1h8v4H4zM1 6h14v6h-3v3H4v-3H1zM5 10v4h6v-4z"/></svg>
      </li>
      <li>thabo@tkkgosana.co.za
        <svg viewBox="0 0 16 16" aria-hidden="true"><path d="M1 3h14v10H1zM2 4.2v.6l6 4 6-4v-.6z"/></svg>
      </li>
    </ul>
  </div>
</section>

<section class="card card-front" aria-label="Business card, brand side">
  <span class="brand-dot"></span>
  <span class="brand-name">TK Kgosana<br>Incorporated</span>
</section>

</body>
</html>
```